<現状の課題>
①一目で、メガネ・コンタクトの取扱いのお店とわからない。
※地域密着型(関東近郊)で隣に眼科が併設されている店舗になります。
②ターゲットにあったサイトデザインになってない。
(詳細は添付”コンセプトワーク”を参照ください)

<現在のサイト>
明確なHPの情報共有はできませんが、トップページの情報を一部伏せて共有します。
添付 ”トップページ” を参照ください。

<イメージサイト>
http://www.mogutart.jp/
写真多めのポップデザインとして
http://www2.kurumiko.co.jp/
コンテンツの配置やメインターゲットへの訴求の仕方
http://www.tobui.jp/
商品、店舗(施設)の見せ方

<重視する点/検討基準>
① デザイン性(ペルソナにあったデザイン)
② 納期厳守

<具体的な制作数>
TOPページ:1ページ

<選考の進め方>
ご提案頂いたデザイン内容・コンセプトなどをもとに、プロジェクトメンバーで選考、決定致します。
※今回は、トップページのデザインのみの見積もりとなります。
今後、コーディングを依頼する可能性もございます。(別途見積もり)

以上です。
Pavonerの皆さまからの、素晴らしい提案をお待ちしております。
宜しくお願い致します。
緑系、黄・オレンジ系、コンセプトカラー(ホワイト6割、グリーン3割、オレンジ1割の配色 ※あくまで弊社のイメージです)
コンセプトカラーもこれから決めていくため、自由に提案頂きたいです。
現在はメインとなるコンセプトカラーを3色ほどで考えています。
※提案数によっては期限延長する場合がございますのでご容赦ください。
※期限6/9⇒6/11へ延長致します。
選定時期は順次報告致します。
ご提案頂いておりました皆様へ

今回、7/2選定期限となっておりましたが、
弊社での選定に時間がかかっております。

誠に申し訳ございませんが、
7/8に期間延長をさせて頂きました。

今しばらくお待ちくださいませ。
今後ともよろしくお願い致します。

当選:hirune2718様
次点:tenbell様、vitre_rousse様
クライアント様と協議させて頂き、総合的なバランスを評価させて頂きました。
その中で、1番クライアント様からお声が多かった「hirune2718様」を当選とさせていただきました。ありがとうございました。

いずれもそれぞれに良いものがあり、大いに悩んで選択させて頂きました。ご提案頂いた皆様に心より感謝申し上げます。

また、今回選定が遅れてしまったこと大変申し訳ございませんでした。

機会があれば、今後ともよろしくお願い致します。

```html
<!DOCTYPE html>
<html lang="ja">
<head>
<meta charset="utf-8">
<title>メガネ・コンタクト 店舗トップ</title>
<link href="https://fonts.googleapis.com/css2?family=M+PLUS+Rounded+1c:wght@400;700;800&family=Noto+Sans+JP:wght@400;500;700&display=swap" rel="stylesheet">
<style>
:root{
  --green:#0f8a1e;
  --green-dark:#0b6b16;
  --green-deep:#0a5a12;
  --lime:#8cc63f;
  --lime-soft:#c7e29a;
  --yellow:#ffd400;
  --red:#e60012;
  --orange:#f08c00;
  --ink:#333;
  --line:#e6e6e6;
  --white:#fff;
}
*{margin:0;padding:0;box-sizing:border-box}
html,body{width:1200px;height:2928px;overflow:hidden}
body{font-family:"Noto Sans JP",sans-serif;color:var(--ink);background:var(--white);position:relative}
.round{font-family:"M PLUS Rounded 1c",sans-serif}

/* header */
.site-header{position:absolute;top:0;left:0;width:1200px;height:56px;border-bottom:4px solid var(--green);background:#fff}
.brand{position:absolute;left:160px;top:0;width:90px;height:52px;background:var(--green);color:#fff;font-weight:700;font-size:16px;display:flex;align-items:center;justify-content:center}
.util{position:absolute;right:150px;top:4px;display:flex;gap:18px;font-size:10px;color:#666}
.gnav{position:absolute;left:590px;top:18px;display:flex}
.gnav a{display:block;width:82px;height:34px;line-height:34px;text-align:center;font-size:13px;font-weight:700;color:var(--green);border-left:1px solid var(--line);text-decoration:none}
.gnav a.shop{background:var(--green);color:#fff;width:110px;font-size:12px}

/* hero */
.hero{position:absolute;top:60px;left:0;width:1200px;height:480px;
  background-image:linear-gradient(#eee 1px,transparent 1px),linear-gradient(90deg,#eee 1px,transparent 1px);background-size:40px 40px}
.hero-badge{position:absolute;left:208px;top:88px;width:100px;height:100px;border-radius:50%;background:var(--orange);color:#fff;font-size:15px;font-weight:800;text-align:center;display:flex;align-items:center;justify-content:center;line-height:1.3}
.hero-lead{position:absolute;left:0;width:1200px;top:110px;text-align:center;font-size:22px;font-weight:800;color:var(--green)}
.hero-lead span{background:linear-gradient(transparent 60%,#ffe36b 60%)}
.hero-pills{position:absolute;top:160px;left:0;width:1200px;display:flex;justify-content:center;gap:34px}
.pill{display:flex;align-items:center;gap:10px;font-size:38px;font-weight:800;color:var(--green)}
.pill i{display:block;width:96px;height:40px;border:4px solid var(--green);border-radius:10px;background:var(--yellow)}
.hero-copy{position:absolute;top:230px;left:0;width:1200px;text-align:center;font-size:36px;font-weight:800;color:var(--green)}
.hero-people{position:absolute;top:290px;left:330px;width:540px;height:200px;border-radius:12px;background:linear-gradient(#f4f8ee,#e3efd2)}
.hero-side{position:absolute;top:270px;width:150px;height:210px;border-radius:12px;background:linear-gradient(#f4f8ee,#e3efd2)}

/* points */
.points{position:absolute;top:560px;left:0;width:1200px;height:380px;background:var(--green)}
.points h2{position:absolute;left:160px;top:32px;color:#fff;font-size:26px;font-weight:700}
.points .sub{position:absolute;left:160px;top:78px;color:#fff;font-size:13px}
.cards{position:absolute;left:160px;top:120px;display:flex;gap:20px}
.card{width:280px;height:180px;background:#fff;border-radius:8px;position:relative;padding:66px 16px 0 140px;font-size:11px;line-height:1.7}
.card .tag{position:absolute;top:-8px;left:0;right:0;height:58px;background:var(--green-dark);border:3px solid #fff;border-radius:10px;color:#fff;text-align:center;padding-top:6px}
.card .tag small{display:block;font-size:11px;color:var(--yellow)}
.card .tag b{font-size:20px}
.card .pic{position:absolute;left:14px;top:66px;width:116px;height:100px;border-radius:6px;background:#e8f2dc}
.points .foot{position:absolute;left:0;width:1200px;top:330px;text-align:center;color:#fff;font-size:12px}

/* campaign */
.sec-title{position:absolute;left:0;width:1200px;text-align:center}
.sec-title small{display:block;font-size:11px;color:#888}
.campaign-title{top:980px}
.campaign-title h2{display:inline-flex;align-items:center;gap:10px;margin-top:8px;font-size:26px;font-weight:800;color:var(--green);border-bottom:3px solid var(--green);padding:4px 24px}
.banner{position:absolute;left:160px;top:1072px;width:880px;height:588px;background:var(--yellow)}
.banner .left{position:absolute;left:40px;top:70px;width:160px;height:160px;border-radius:50%;background:var(--red);color:#fff;font-size:24px;font-weight:800;text-align:center;display:flex;align-items:center;justify-content:center;line-height:1.2}
.banner .right{position:absolute;right:40px;top:80px;width:160px;height:160px;border-radius:50%;background:#fff;border:4px solid var(--red);color:var(--red);font-size:36px;font-weight:800;text-align:center;display:flex;align-items:center;justify-content:center;line-height:1.1}
.banner .ribbon{position:absolute;left:260px;top:60px;width:360px;text-align:center;color:var(--red);font-size:14px;font-weight:700}
.banner .price{position:absolute;left:230px;top:88px;width:420px;height:110px;background:var(--red);color:#fff;font-size:72px;font-weight:800;text-align:center;line-height:110px}
.banner .glasses{position:absolute;left:240px;top:240px;width:400px;height:160px;border-radius:20px;background:linear-gradient(#ffe866,#f7c900)}
.banner .headline{position:absolute;left:0;width:880px;top:420px;text-align:center;font-size:36px;font-weight:800;color:#222}
.banner .note{position:absolute;left:0;width:880px;top:490px;text-align:center;font-size:11px;color:#555}

/* news */
.news{position:absolute;top:1764px;left:160px;width:880px;height:380px;
  background-image:linear-gradient(#eee 1px,transparent 1px),linear-gradient(90deg,#eee 1px,transparent 1px);background-size:40px 40px}
.news h2{font-size:22px;font-weight:700;color:var(--green);margin-top:48px}
.news ul{list-style:none;width:600px;margin-top:14px;border-top:2px solid var(--green)}
.news li{display:flex;gap:20px;padding:12px 0;border-bottom:1px dotted #bbb;font-size:12px}
.news li time{color:#777;width:70px}
.news li p{line-height:1.7}
.news li b{color:var(--ink)}
.side-links{position:absolute;right:0;top:30px;display:flex;flex-direction:column;gap:14px}
.side-links a{display:flex;align-items:center;gap:12px;width:220px;height:56px;background:var(--green);color:#fff;font-size:15px;font-weight:700;padding-left:20px;text-decoration:none;border-radius:4px}
.side-links a i{width:24px;height:24px;border:2px solid #fff;border-radius:4px}

/* shop banner */
.shop-banner{position:absolute;left:160px;top:2220px;width:880px;height:300px;background:var(--lime);border-radius:6px}
.shop-banner .inner{position:absolute;inset:16px;border:3px solid #fff;border-radius:4px}
.shop-banner .bubble{position:absolute;left:150px;top:40px;background:var(--yellow);color:var(--green-deep);font-size:13px;font-weight:700;padding:6px 18px;border-radius:14px}
.shop-banner .staff{position:absolute;left:50px;top:60px;width:110px;height:180px;border-radius:10px;background:#b5da80}
.shop-banner h3{position:absolute;left:180px;top:84px;font-size:46px;font-weight:800;color:#fff}
.shop-banner .en{position:absolute;left:260px;top:170px;width:520px;height:60px;border:3px solid #fff;border-radius:30px;color:#fff;font-size:30px;font-weight:800;text-align:center;line-height:54px;letter-spacing:.05em}

/* to top */
.to-top{position:absolute;left:568px;top:2588px;width:64px;height:64px;border-radius:50%;background:var(--green-dark);display:flex;align-items:center;justify-content:center}
.to-top-label{position:absolute;left:0;width:1200px;top:2664px;text-align:center;font-size:10px;color:#888}

/* footer */
.site-footer{position:absolute;top:2752px;left:0;width:1200px;height:176px;background:var(--green-deep);color:#fff}
.fnav{position:absolute;left:160px;top:40px;display:flex;gap:10px}
.fnav a{width:70px;height:52px;background:#fff;color:var(--green);font-size:11px;font-weight:700;display:flex;align-items:flex-end;justify-content:center;padding-bottom:6px;border-radius:3px;text-decoration:none}
.fnav a.shop{background:var(--lime);color:#fff}
.fnav a.alt{background:var(--orange);color:#fff}
.flinks{position:absolute;right:160px;top:48px;display:flex;gap:18px;font-size:11px}
.flinks.second{top:80px}
.copy{position:absolute;left:160px;top:120px;font-size:10px;color:#cfe3c9}
</style>
</head>
<body>

<header class="site-header">
  <div class="brand">ロゴ</div>
  <div class="util"><span>店舗情報</span><span>採用情報</span><span>よくある質問</span><span>お問合せ</span></div>
  <nav class="gnav">
    <a>メガネ</a><a>コンタクト</a><a>クーポン</a><a>お客様の声</a><a>店舗情報</a><a class="shop">コンタクト通販</a>
  </nav>
</header>

<section class="hero round">
  <div class="hero-badge">眼科が<br>となりに<br>あります</div>
  <p class="hero-lead"><span>眼科が隣接しているから安心</span></p>
  <div class="hero-pills">
    <div class="pill"><i></i>メガネ</div>
    <div class="pill"><i></i>コンタクト</div>
  </div>
  <p class="hero-copy">は当店にお任せください!!</p>
  <div class="hero-side" style="left:160px" role="img" aria-label="メガネをかけた女性スタッフのイラスト"></div>
  <div class="hero-people" role="img" aria-label="メガネをかけた家族のイラスト"></div>
  <div class="hero-side" style="left:890px" role="img" aria-label="コンタクトを勧める女性のイラスト"></div>
</section>

<section class="points">
  <h2 class="round">家族の目を守りたいから…</h2>
  <p class="sub">眼科に隣接しているお店だからこそ、ほんとに安心できるサービスをお届けします。</p>
  <div class="cards">
    <div class="card"><div class="tag"><small>ポイント その1</small><b class="round">となりに眼科</b></div><div class="pic" role="img" aria-label="眼科の建物のイラスト"></div>お店のとなりに眼科があるので、気軽に検査を受けていただけます。</div>
    <div class="card"><div class="tag"><small>ポイント その2</small><b class="round">すぐに対応</b></div><div class="pic" role="img" aria-label="スタッフ対応のイラスト"></div>度数の変化や急なトラブルにも、その日のうちに対応いたします。</div>
    <div class="card"><div class="tag"><small>ポイント その3</small><b class="round">専任スタッフ</b></div><div class="pic" role="img" aria-label="専任スタッフのイラスト"></div>専門知識をもつスタッフが、お客様に合うメガネを一緒に選びます。</div>
  </div>
  <p class="foot">メガネ・コンタクトのことならお気軽にご相談ください。</p>
</section>

<div class="sec-title campaign-title">
  <small>期間限定！お得なキャンペーン実施中！</small>
  <h2 class="round"><svg width="34" height="16" viewBox="0 0 34 16"><g fill="none" stroke="#0f8a1e" stroke-width="2.5"><rect x="2" y="3" width="12" height="10" rx="3"/><rect x="20" y="3" width="12" height="10" rx="3"/><path d="M14 7h6"/></g></svg>キャンペーン情報</h2>
</div>

<section class="banner round">
  <div class="left">下取り<br>メガネ<br>1本ごと</div>
  <p class="ribbon">今だけ！期間限定！</p>
  <div class="price">¥1,000</div>
  <div class="right">8/12<br><span style="font-size:26px">まで!</span></div>
  <div class="glasses" role="img" aria-label="黒縁メガネのイラスト"></div>
  <p class="headline">古いメガネ下取りします</p>
  <p class="note">お使いのメガネをお持ちください。新しいメガネのご購入時に1本につき1,000円を値引きいたします。</p>
</section>

<section class="news">
  <h2 class="round">新着情報</h2>
  <ul>
    <li><time>2018.8.1</time><p><b>hogehogeメガネ ご予約開始時期について</b><br>大人気の hogehogeメガネ 予約開始日が決定しました…</p></li>
    <li><time>2018.8.1</time><p><b>hogehogeメガネ ご予約開始時期について</b><br>大人気の hogehogeメガネ 予約開始日が決定しました…</p></li>
    <li><time>2018.8.1</time><p><b>hogehogeメガネ ご予約開始時期について</b><br>大人気の hogehogeメガネ 予約開始日が決定しました…</p></li>
  </ul>
  <div class="side-links">
    <a><i></i>会社概要</a><a><i></i>採用情報</a><a><i></i>お問合せ</a>
  </div>
</section>

<section class="shop-banner round">
  <div class="inner"></div>
  <div class="staff" role="img" aria-label="案内するスタッフのイラスト"></div>
  <p class="bubble">もっと便利に！もっと手軽に！</p>
  <h3>コンタクト、通販で買えます</h3>
  <div class="en">CONTACT WEB SHOP</div>
</section>

<a class="to-top"><svg width="24" height="16" viewBox="0 0 24 16"><path d="M3 13l9-9 9 9" fill="none" stroke="#fff" stroke-width="3"/></svg></a>
<p class="to-top-label">このページのトップへ</p>

<footer class="site-footer">
  <nav class="fnav">
    <a>メガネ</a><a>コンタクト</a><a>クーポン</a><a>お客様の声</a><a>店舗情報</a><a class="shop">通販</a><a class="alt">求人</a>
  </nav>
  <div class="flinks"><span>会社概要</span><span>採用情報</span><span>お問合せ</span></div>
  <div class="flinks second"><span>個人情報について</span><span>サイトマップ</span></div>
  <p class="copy">Copyright © 2018 Sample Optical. All rights reserved.</p>
</footer>

</body>
</html>
```